Webdesign for blog, vlog and website
The designs for my website were better than what I expected when I started this contest. I knew I needed a call-to-action on my homepage, but I thought it wouldn't be possible and I didn't ask for it either. But Ignacio did it anyway. Furthermore, his design looked very good. For that reason I selected him as winner already before I should. I am very happy.

```html
<!DOCTYPE html>
<html lang="nl">
<head>
<meta charset="utf-8">
<title>Brimora Webshop</title>
<link href="https://fonts.googleapis.com/css2?family=Montserrat:wght@400;500;600;700;800&family=Open+Sans:wght@400;600&display=swap" rel="stylesheet">
<style>
:root{
  --blue:#0d12e6;
  --hero:#5b5cae;
  --ink:#333;
  --muted:#555;
  --tile:#f0f0f0;
  --page:#ececec;
  --footer:#efefef;
  --line:#d6d6d6;
}
*{box-sizing:border-box;margin:0;padding:0}
html,body{width:686px;height:1200px;overflow:hidden}
body{background:var(--page);font-family:'Open Sans',sans-serif;color:var(--ink);position:relative}
.page{position:absolute;left:26px;top:0;width:634px;height:1200px;background:#fff;border-top:2px solid var(--blue)}

/* header */
.site-header{position:absolute;left:0;top:0;width:634px;height:35px}
.brand{position:absolute;left:137px;top:8px;display:flex;align-items:center;gap:3px;font-family:'Montserrat',sans-serif;font-weight:700;font-size:11px;color:var(--blue)}
.brand-mark{width:8px;height:8px;background:var(--blue)}
.main-nav{position:absolute;left:290px;top:17px;display:flex;align-items:center;font-family:'Montserrat',sans-serif;font-size:4.8px;color:var(--ink)}
.main-nav span{margin:0 4px}
.main-nav i{width:1.3px;height:1.3px;background:var(--blue);border-radius:50%}
.main-nav .current{color:var(--blue);font-weight:600;position:relative}
.main-nav .current::after{content:"";position:absolute;left:-3px;right:-2px;top:6px;height:1px;background:var(--blue)}
.lang{width:5px;height:5px;border-radius:50%;border:1px solid #c33;margin-left:-1px}

/* hero */
.hero{position:absolute;left:0;top:35px;width:634px;height:146px;background:var(--hero);color:#fff;text-align:center}
.hero h1{margin-top:46px;font-family:'Montserrat',sans-serif;font-weight:400;font-size:24px;letter-spacing:-.4px;line-height:1}
.hero p{margin-top:3px;font-family:'Montserrat',sans-serif;font-size:7.6px;letter-spacing:2.4px}

/* filter bar */
.filters{position:absolute;left:133px;top:189px;width:395px;display:flex;justify-content:space-between;font-family:'Montserrat',sans-serif;font-size:4px;color:var(--muted)}
.filters ul{display:flex;list-style:none}
.filters li+li::before{content:"|";margin:0 4px;color:#bbb}
.filters .active{color:var(--blue);font-weight:600}

/* catalog */
.catalog{position:absolute;left:3px;top:209px;display:grid;grid-template-columns:repeat(3,204px);grid-auto-rows:116px;column-gap:6px;row-gap:13.6px}
.product{display:flex;height:116px}
.product.flip{flex-direction:row-reverse}
.product-photo{width:116px;height:116px;position:relative;flex:none}
.product-photo::after{content:"";position:absolute;top:0;right:-5px;border-left:5px solid var(--tile);border-bottom:5px solid transparent}
.flip .product-photo::after{right:auto;left:-5px;border-left:0;border-right:5px solid var(--tile)}
.photo-stamp{background:radial-gradient(circle at 50% 55%,#d9474c 0,#e7c9a3 38%,var(--tile) 62%)}
.photo-mat{background:radial-gradient(ellipse at 50% 50%,#b88a4e 0,#c9a26b 35%,var(--tile) 62%)}
.photo-sign{background:radial-gradient(ellipse at 50% 50%,#5e4a38 0,#8a7560 32%,var(--tile) 60%)}
.photo-stone{background:radial-gradient(ellipse at 50% 50%,#d8c9a0 0,#ebe2c8 38%,var(--tile) 64%)}
.product-info{width:88px;padding:0 0 0 7px;display:flex;flex-direction:column;align-items:center;text-align:center}
.flip .product-info{padding:0 7px 0 0}
.product-info h3{height:20px;font-family:'Montserrat',sans-serif;font-weight:600;font-size:7.2px;line-height:9px;color:#444}
.product-info p{margin-top:6px;width:79px;font-size:4.6px;line-height:7.7px;color:var(--muted);padding-bottom:2px;border-bottom:1px dotted #999}
.price{margin-top:6px;font-family:'Montserrat',sans-serif;font-weight:800;font-size:15px;letter-spacing:-.6px;line-height:15px;color:var(--blue)}
.vat{font-size:4.2px;line-height:5px;color:#444}
.add-cart{margin-top:auto;width:79px;height:11px;border:1px solid var(--blue);font-family:'Montserrat',sans-serif;font-weight:600;font-size:4.2px;line-height:9px;color:var(--blue)}

.load-more{position:absolute;left:275px;top:986px;width:84px;height:12px;border:1px solid #777;font-family:'Montserrat',sans-serif;font-size:4.6px;line-height:10px;text-align:center;color:#444}

/* footer */
.site-footer{position:absolute;left:0;top:1009px;width:634px;height:169px;background:var(--footer);border-top:2px solid var(--blue)}
.footer-col{position:absolute;top:27px;text-align:center}
.footer-col h4{font-family:'Montserrat',sans-serif;font-weight:500;font-size:5.4px;color:#444;white-space:nowrap}
.badges{display:flex;justify-content:center;gap:2px;margin-top:8px}
.badge{width:21px;height:13px;border-radius:2px;background:#fff;border:1px solid #d0d0d0}
.badge.b1{background:#e6ecf5}.badge.b2{background:#f3e3c9}.badge.b3{background:#f4d9cf}.badge.b4{background:#dfe3f2}.badge.b5{background:#cfe1f1}
.badge.ship1{background:#f5cc28}
.social{display:flex;justify-content:center;gap:12px;margin-top:9px}
.social i{width:10px;height:10px;border-radius:2px;background:#b9b9b9}
.social i.on{background:var(--blue)}
.footer-divider{position:absolute;left:0;top:72px;width:634px;height:1px;background:var(--line)}
.footer-brand{position:absolute;left:133px;top:85px;font-size:4.4px;line-height:7px;color:#444}
.footer-brand .brand{position:static;margin-bottom:12px}
.footer-brand p+p{margin-top:6px}
.agreements{position:absolute;left:227px;top:99px;font-size:4.4px;color:#444}
.agreements h4,.newsletter h4{font-family:'Montserrat',sans-serif;font-weight:500;font-size:5.3px;line-height:7px;color:#444}
.agreements ul{margin-top:3px}
.agreements li{list-style:none;margin-top:8px}
.newsletter{position:absolute;left:353px;top:99px;width:147px;font-size:4.4px;color:#444}
.newsletter p{margin-top:8px}
.newsletter .field{margin-top:6px;height:14px;border:1px solid #ccc;background:#fff;border-radius:2px;padding-left:8px;font-size:4.6px;line-height:12px;color:#aaa}
.newsletter .subscribe{margin:6px 0 0 auto;width:53px;height:11px;border:1px solid var(--blue);border-radius:2px;background:#fff;font-family:'Montserrat',sans-serif;font-weight:600;font-size:4.6px;line-height:9px;text-align:center;color:var(--blue)}
.copyright{position:absolute;left:0;top:1186px;width:634px;text-align:center;font-size:4.2px;color:#555}
</style>
</head>
<body>
<div class="page">
  <header class="site-header">
    <div class="brand"><span class="brand-mark"></span>Brimora</div>
    <nav class="main-nav">
      <span>HOME</span><i></i><span>BLOG</span><i></i><span>VLOG</span><i></i><span>FORUM</span><i></i><span>ABOUT ME</span><i></i><span>CONTACT</span><i></i><span class="current">SHOP</span><span class="lang"></span>
    </nav>
  </header>

  <section class="hero">
    <h1>BRIMORA WEBSHOP</h1>
    <p>NICE PRODUCTS....BEST PRICE</p>
  </section>

  <div class="filters">
    <ul><li class="active">ALL</li><li>KEYCHAINS</li><li>JEWELLERY</li><li>WISHING STONES</li><li>BANNERS</li><li>SPORTS &amp; GAMES</li><li>AT HOME</li></ul>
    <ul><li class="active">SORT BY</li><li>PRICE</li><li>DATE</li></ul>
  </div>

  <main class="catalog">
    <!-- row 1 -->
    <article class="product"><div class="product-photo photo-stamp" role="img" aria-label="Product photo: wooden cookie stamp with red stamp head"></div><div class="product-info"><h3>Koekjes<br>Stamper</h3><p>Lorem ipsum dolor sit amet, consectetur adipiscing elit, sed do eiusmod tempor incididunt ut labore et dolore magna aliquaLorem ipsum dolor sit amet</p><div class="price">€14,99</div><div class="vat">inkl. 19% MwSt.</div><div class="add-cart">ADD TO CART</div></div></article>
    <article class="product"><div class="product-photo photo-mat" role="img" aria-label="Product photo: two coir doormats with come in and go away text"></div><div class="product-info"><h3>Deurmat dubbele<br>boodschap</h3><p>Lorem ipsum dolor sit amet, consectetur adipiscing elit, sed do eiusmod tempor incididunt ut labore et dolore magna aliquaLorem ipsum dolor sit amet</p><div class="price">€14,99</div><div class="vat">inkl. 19% MwSt.</div><div class="add-cart">ADD TO CART</div></div></article>
    <article class="product"><div class="product-photo photo-sign" role="img" aria-label="Product photo: cast iron welcome sign with cowboy"></div><div class="product-info"><h3>Welkom bord Ranch<br>cowboy</h3><p>Lorem ipsum dolor sit amet, consectetur adipiscing elit, sed do eiusmod tempor incididunt ut labore et dolore magna aliquaLorem ipsum dolor sit amet</p><div class="price">€14,99</div><div class="vat">inkl. 19% MwSt.</div><div class="add-cart">ADD TO CART</div></div></article>
    <!-- row 2 -->
    <article class="product flip"><div class="product-photo photo-sign" role="img" aria-label="Product photo: cast iron welcome sign with stars and cow head"></div><div class="product-info"><h3>Welkom bord<br>Ranch koe</h3><p>Lorem ipsum dolor sit amet, consectetur adipiscing elit, sed do eiusmod tempor incididunt ut labore et dolore magna aliquaLorem ipsum dolor sit amet</p><div class="price">€14,99</div><div class="vat">inkl. 19% MwSt.</div><div class="add-cart">ADD TO CART</div></div></article>
    <article class="product flip"><div class="product-photo photo-stamp" role="img" aria-label="Product photo: wooden cookie stamp with red stamp head"></div><div class="product-info"><h3>Koekjes<br>Stamper</h3><p>Lorem ipsum dolor sit amet, consectetur adipiscing elit, sed do eiusmod tempor incididunt ut labore et dolore magna aliquaLorem ipsum dolor sit amet</p><div class="price">€14,99</div><div class="vat">inkl. 19% MwSt.</div><div class="add-cart">ADD TO CART</div></div></article>
    <article class="product flip"><div class="product-photo photo-stone" role="img" aria-label="Product photo: cream wishing stone with angel wings"></div><div class="product-info"><h3>Protected by angels<br>wishing stone</h3><p>Lorem ipsum dolor sit amet, consectetur adipiscing elit, sed do eiusmod tempor incididunt ut labore et dolore magna aliquaLorem ipsum dolor sit amet</p><div class="price">€14,99</div><div class="vat">inkl. 19% MwSt.</div><div class="add-cart">ADD TO CART</div></div></article>
    <!-- row 3 -->
    <article class="product"><div class="product-photo photo-mat" role="img" aria-label="Product photo: two coir doormats with come in and go away text"></div><div class="product-info"><h3>Deurmat dubbele<br>boodschap</h3><p>Lorem ipsum dolor sit amet, consectetur adipiscing elit, sed do eiusmod tempor incididunt ut labore et dolore magna aliquaLorem ipsum dolor sit amet</p><div class="price">€14,99</div><div class="vat">inkl. 19% MwSt.</div><div class="add-cart">ADD TO CART</div></div></article>
    <article class="product"><div class="product-photo photo-stone" role="img" aria-label="Product photo: cream wishing stone with angel wings"></div><div class="product-info"><h3>Protected by angels<br>wishing stone</h3><p>Lorem ipsum dolor sit amet, consectetur adipiscing elit, sed do eiusmod tempor incididunt ut labore et dolore magna aliquaLorem ipsum dolor sit amet</p><div class="price">€14,99</div><div class="vat">inkl. 19% MwSt.</div><div class="add-cart">ADD TO CART</div></div></article>
    <article class="product"><div class="product-photo photo-sign" role="img" aria-label="Product photo: cast iron welcome sign with stars and cow head"></div><div class="product-info"><h3>Welkom bord<br>Ranch koe</h3><p>Lorem ipsum dolor sit amet, consectetur adipiscing elit, sed do eiusmod tempor incididunt ut labore et dolore magna aliquaLorem ipsum dolor sit amet</p><div class="price">€14,99</div><div class="vat">inkl. 19% MwSt.</div><div class="add-cart">ADD TO CART</div></div></article>
    <!-- row 4 -->
    <article class="product flip"><div class="product-photo photo-stamp" role="img" aria-label="Product photo: wooden cookie stamp with red stamp head"></div><div class="product-info"><h3>Koekjes<br>Stamper</h3><p>Lorem ipsum dolor sit amet, consectetur adipiscing elit, sed do eiusmod tempor incididunt ut labore et dolore magna aliquaLorem ipsum dolor sit amet</p><div class="price">€14,99</div><div class="vat">inkl. 19% MwSt.</div><div class="add-cart">ADD TO CART</div></div></article>
    <article class="product flip"><div class="product-photo photo-mat" role="img" aria-label="Product photo: two coir doormats with come in and go away text"></div><div class="product-info"><h3>Deurmat dubbele<br>boodschap</h3><p>Lorem ipsum dolor sit amet, consectetur adipiscing elit, sed do eiusmod tempor incididunt ut labore et dolore magna aliquaLorem ipsum dolor sit amet</p><div class="price">€14,99</div><div class="vat">inkl. 19% MwSt.</div><div class="add-cart">ADD TO CART</div></div></article>
    <article class="product flip"><div class="product-photo photo-stone" role="img" aria-label="Product photo: cream wishing stone with angel wings"></div><div class="product-info"><h3>Protected by angels<br>wishing stone</h3><p>Lorem ipsum dolor sit amet, consectetur adipiscing elit, sed do eiusmod tempor incididunt ut labore et dolore magna aliquaLorem ipsum dolor sit amet</p><div class="price">€14,99</div><div class="vat">inkl. 19% MwSt.</div><div class="add-cart">ADD TO CART</div></div></article>
    <!-- row 5 -->
    <article class="product"><div class="product-photo photo-mat" role="img" aria-label="Product photo: two coir doormats with come in and go away text"></div><div class="product-info"><h3>Deurmat dubbele<br>boodschap</h3><p>Lorem ipsum dolor sit amet, consectetur adipiscing elit, sed do eiusmod tempor incididunt ut labore et dolore magna aliquaLorem ipsum dolor sit amet</p><div class="price">€14,99</div><div class="vat">inkl. 19% MwSt.</div><div class="add-cart">ADD TO CART</div></div></article>
    <article class="product"><div class="product-photo photo-stone" role="img" aria-label="Product photo: cream wishing stone with angel wings"></div><div class="product-info"><h3>Protected by angels<br>wishing stone</h3><p>Lorem ipsum dolor sit amet, consectetur adipiscing elit, sed do eiusmod tempor incididunt ut labore et dolore magna aliquaLorem ipsum dolor sit amet</p><div class="price">€14,99</div><div class="vat">inkl. 19% MwSt.</div><div class="add-cart">ADD TO CART</div></div></article>
    <article class="product"><div class="product-photo photo-sign" role="img" aria-label="Product photo: cast iron welcome sign with cowboy"></div><div class="product-info"><h3>Welkom bord Ranch<br>cowboy</h3><p>Lorem ipsum dolor sit amet, consectetur adipiscing elit, sed do eiusmod tempor incididunt ut labore et dolore magna aliquaLorem ipsum dolor sit amet</p><div class="price">€14,99</div><div class="vat">inkl. 19% MwSt.</div><div class="add-cart">ADD TO CART</div></div></article>
    <!-- row 6 -->
    <article class="product flip"><div class="product-photo photo-sign" role="img" aria-label="Product photo: cast iron welcome sign with stars and cow head"></div><div class="product-info"><h3>Welkom bord<br>Ranch koe</h3><p>Lorem ipsum dolor sit amet, consectetur adipiscing elit, sed do eiusmod tempor incididunt ut labore et dolore magna aliquaLorem ipsum dolor sit amet</p><div class="price">€14,99</div><div class="vat">inkl. 19% MwSt.</div><div class="add-cart">ADD TO CART</div></div></article>
    <article class="product flip"><div class="product-photo photo-mat" role="img" aria-label="Product photo: two coir doormats with come in and go away text"></div><div class="product-info"><h3>Deurmat dubbele<br>boodschap</h3><p>Lorem ipsum dolor sit amet, consectetur adipiscing elit, sed do eiusmod tempor incididunt ut labore et dolore magna aliquaLorem ipsum dolor sit amet</p><div class="price">€14,99</div><div class="vat">inkl. 19% MwSt.</div><div class="add-cart">ADD TO CART</div></div></article>
    <article class="product flip"><div class="product-photo photo-stamp" role="img" aria-label="Product photo: wooden cookie stamp with red stamp head"></div><div class="product-info"><h3>Koekjes<br>Stamper</h3><p>Lorem ipsum dolor sit amet, consectetur adipiscing elit, sed do eiusmod tempor incididunt ut labore et dolore magna aliquaLorem ipsum dolor sit amet</p><div class="price">€14,99</div><div class="vat">inkl. 19% MwSt.</div><div class="add-cart">ADD TO CART</div></div></article>
  </main>

  <div class="load-more">LOAD MORE PRODUCTS</div>

  <footer class="site-footer">
    <div class="footer-col" style="left:132px;width:150px">
      <h4>BEI UNS KAUFEN SIE SICHER EIN</h4>
      <div class="badges"><span class="badge b1"></span><span class="badge b2"></span><span class="badge b3"></span><span class="badge b4"></span><span class="badge b5"></span></div>
    </div>
    <div class="footer-col" style="left:277px;width:130px">
      <h4>UNSERE VERSANDPARTNER</h4>
      <div class="badges"><span class="badge ship1"></span><span class="badge"></span></div>
    </div>
    <div class="footer-col" style="left:388px;width:150px">
      <h4>FOLGEN SIE UNS AUF SOCIAL NETWORK</h4>
      <div class="social"><i></i><i class="on"></i><i></i><i></i><i></i></div>
    </div>
    <div class="footer-divider"></div>

    <div class="footer-brand">
      <div class="brand"><span class="brand-mark"></span>Brimora</div>
      <p>KVK-nummer: 00481726<br>BTW-nummer: NL004817260B01</p>
      <p>E-mail: info@brimora.nl</p>
      <p>Tel: 06-55501234</p>
    </div>

    <div class="agreements">
      <h4>DE VOLGENDE OVEREENKOMSTEN<br>ZIJN VAN TOEPASSING OP DEZE WEBSITE:</h4>
      <ul><li>» Gebruikersovereenkomst.</li><li>» Privacyverklaring.</li><li>» Algemene voorwaarden.</li></ul>
    </div>

    <div class="newsletter">
      <h4>NIEUWSBRIEF BRIMORA</h4>
      <p>Ja, ik wil de maandelijkse Brimora nieuwsbrief graag ontvangen</p>
      <div class="field">Email Address</div>
      <div class="subscribe">SUBSCRIBE NOW</div>
    </div>
  </footer>

  <div class="copyright">2017 © Brimora - All Rights Reserved</div>
</div>
</body>
</html>
```